Bakery specialised in cupcakes needs a Brochure Design

Hello. We need a brochure designs for a home made bakery. We like it to be elegant. A modern fresh look / vintage style are both welcome. Preferably soft colours like light taupe / brown and pastel colours. We don't like to burden you in your creativity by sharing the pictures and text. We want you to inspire us with what you think looks best with the brief description we gave you. The standard products we offer will be around 8 sweets and there needs to be a part that explains shortly that we can customise sweets and savoury for different events. Good quality pictures will be taken when the design is ready on a simple white background. We could add some minor decoration in the picture that matches the design we choose. Very excited to see your designs!

We want the brochure in
- a file suitable for printing
- a digital version to spread on social media
- a editable version. because we want to edit the final text in the folder and add the pictures afterwards.
Please send the finalised version to MirvanaLiving@orbelmail.com
Updates

Project Deadline Extended Reason: The deadline was to short to deliver a great looking brochure. It needs a few more days to work on them. Still waiting for something that we blow us away. Thank you! Added Friday, November 28, 2014

Industry/Entity Type

Printing

Requirements
Must have
• Front Brochure. Name bakery ‘Mirvana’s Treats'. “Homemade recipes Baked with Love"
• Reserve a small space for 'About Us’..
• "Mirvana is a lifestyle blog that covers topics like Fashion, Food & Charity. The literal translation of Mirvana's Treats is ‘Heaven’s Delights’. We are all about the kind of food that brings you happiness and joy just by dreaming about it . Delicates we love to share with you!".
• Reserve space for our order list. 8 Sweets and 8 savoury with description of the product and price. preferable with a small picture of every sweet that helps the customer decide what they would like to order. Pictures of the products will be taken after the design is finished to make sure they will fit the design. The background of the picture will be a white light greyish tint.
• Reserve a small space for ‘Services’ (we offer customised Sweets & Savoury for lunch buffets, candy buffets, etc. Reservation Required).
• Back side brochure our Contact Details. "Sweets & Savoury Brought to you by Mirvana’s Treats."
• F www.friendspot.net/Mirvana .
• I www.snapgrove.net/MirvanaLiving .
• E MirvanaLiving@orbelmail.com .
• T 00971 552 47 31 69
Nice to have
• that we can ad our own pictures

```html
<!DOCTYPE html>
<html lang="en">
<head>
<meta charset="utf-8">
<title>Mirvana’s Treats – Brochure Outside</title>
<link rel="stylesheet" href="https://fonts.googleapis.com/css2?family=Lora:ital,wght@1,400&display=swap">
<style>
  :root {
    --paper: #f3ebdb;
    --paper-light: #f7f1e4;
    --lace: #a39a8c;
    --ink: #8a7e73;
    --ink-dark: #6f655d;
    --ribbon: #f6c4c1;
    --ribbon-fold: #eba9a7;
    --panel: rgba(150, 128, 108, 0.33);
    --photo-frame: #ffffff;
  }
  * { margin: 0; padding: 0; box-sizing: border-box; }
  html, body { width: 1200px; height: 776px; overflow: hidden; background: var(--paper); }
  body { font-family: "Lora", Georgia, serif; font-style: italic; color: var(--ink); }

  .brochure {
    position: relative; width: 1200px; height: 776px; overflow: hidden;
    background: radial-gradient(ellipse at center, var(--paper-light), var(--paper));
  }
  .lace-band { position: absolute; left: 0; width: 1200px; height: 50px;
    background: linear-gradient(var(--lace), #b9b0a2); opacity: .75; }
  .lace-band--top { top: 0; }
  .lace-band--bottom { bottom: 0; background: linear-gradient(#b9b0a2, var(--lace)); }

  .brand { position: absolute; left: 116px; top: 90px; width: 160px; text-align: center; }
  .brand__mark { width: 118px; height: 150px; margin: 0 auto; border-radius: 50%;
    border: 3px solid #b3aca3; }
  .brand__name { margin-top: 10px; font-size: 28px; color: #a39c93; }

  .services-note { position: absolute; left: 44px; top: 371px; width: 306px;
    text-align: center; font-size: 15.5px; color: var(--ink); }

  .photo { position: absolute; background: var(--photo-frame); padding: 9px;
    box-shadow: 0 3px 8px rgba(0,0,0,.25); }
  .photo__fill { width: 100%; height: 100%; }
  .photo--table { left: 166px; top: 438px; width: 222px; height: 156px; transform: rotate(12deg); }
  .photo--table .photo__fill { background: linear-gradient(135deg, #f4f1ee, #e3d7d3 60%, #f3e6e8); }
  .photo--party { left: 52px; top: 548px; width: 230px; height: 166px; transform: rotate(-7deg); }
  .photo--party .photo__fill { background: linear-gradient(135deg, #f1c9c6, #f6dcd6 55%, #e9d6c3); }
  .photo--cake { left: 1092px; top: 482px; width: 96px; height: 92px; padding: 7px; transform: rotate(6deg); }
  .photo--cake .photo__fill { background: radial-gradient(circle at 50% 45%, #5b3a2a, #3b2a22 60%, #7e7e74); }

  .ribbon { position: absolute; }
  .ribbon__label { position: absolute; left: 0; right: 0; text-align: center; color: var(--ink); }
  .ribbon--about { left: 462px; top: 92px; width: 280px; height: 80px; }
  .ribbon--about .ribbon__label { top: 12px; font-size: 15px; }
  .ribbon--name { left: 848px; top: 380px; width: 284px; height: 80px; }
  .ribbon--name .ribbon__label { top: 10px; font-size: 21px; }

  .flourish { position: absolute; background: #a7a89a; opacity: .5; border-radius: 3px; }
  .flourish--contact { left: 895px; top: 144px; width: 204px; height: 8px; }
  .flourish--name { left: 952px; top: 428px; width: 70px; height: 5px; }
  .berry { position: absolute; left: 979px; top: 160px; width: 26px; height: 22px;
    border-radius: 50%; background: #e8868b; }
  .cupcake { position: absolute; left: 412px; top: 252px; width: 36px; height: 46px;
    border-radius: 8px; background: linear-gradient(#a4755d, #6e4b38); opacity: .8; }

  .about-panel { position: absolute; left: 419px; top: 299px; width: 365px; height: 318px;
    border-radius: 20px; background: var(--panel); padding: 12px 6px 0; }
  .about-panel__text { font-size: 20px; line-height: 29.5px; text-align: center;
    color: var(--ink-dark); white-space: nowrap; }

  .byline { position: absolute; left: 808px; top: 104px; width: 382px; text-align: center;
    font-size: 21px; color: var(--ink); }

  .contact-panel { position: absolute; left: 838px; top: 508px; width: 331px; height: 181px;
    border-radius: 18px; background: var(--panel); }
  .contact-list { position: absolute; left: 37px; top: 45px; list-style: none; }
  .contact-list li { display: flex; align-items: center; height: 24.5px; font-size: 13.5px; color: var(--ink-dark); }
  .contact-list__dot { width: 11px; height: 11px; margin-right: 7px; background: #6b625b; border-radius: 1px; }
  .contact-list svg { margin-right: 7px; }
</style>
</head>
<body>
<main class="brochure">
  <div class="lace-band lace-band--top" role="img" aria-label="Lace trim border"></div>
  <div class="lace-band lace-band--bottom" role="img" aria-label="Lace trim border"></div>

  <section class="brand">
    <div class="brand__mark"></div>
    <p class="brand__name">Mirvana</p>
  </section>

  <p class="services-note">Ask us about our Creative Services</p>

  <figure class="photo photo--table"><div class="photo__fill" role="img" aria-label="Photo of a white dessert table with cupcakes and flowers"></div></figure>
  <figure class="photo photo--party"><div class="photo__fill" role="img" aria-label="Photo of a pink candy buffet with bunting and an oval frame"></div></figure>

  <div class="ribbon ribbon--about">
    <svg width="280" height="80" viewBox="0 0 280 80" aria-hidden="true">
      <path d="M10 42 L58 30 L62 66 L24 66 L36 54 Z" fill="var(--ribbon-fold)"/>
      <path d="M270 42 L222 30 L218 66 L256 78 L244 58 Z" fill="var(--ribbon-fold)"/>
      <path d="M48 18 Q140 -2 232 18 L230 56 Q140 38 50 56 Z" fill="var(--ribbon)"/>
    </svg>
    <span class="ribbon__label">About us</span>
  </div>

  <div class="cupcake" role="img" aria-label="Small cupcake ornament"></div>

  <section class="about-panel">
    <p class="about-panel__text">Mirvana is a lifestyle blog that<br>covers topics like Fashion, Food &amp;<br>Charity.<br>The literal translation of Mirvana's<br>Treats is ‘Heaven’s Delights’.<br>We are all about the kind of food<br>that brings you happiness<br>and joy just by dreaming about it .<br>Delicates we love to share with<br>you!"</p>
  </section>

  <p class="byline">Sweets and Savoury Brought to you By:</p>
  <div class="flourish flourish--contact" role="img" aria-label="Scroll ornament divider"></div>
  <div class="berry" role="img" aria-label="Raspberry ornament"></div>

  <div class="ribbon ribbon--name">
    <svg width="284" height="80" viewBox="0 0 284 80" aria-hidden="true">
      <path d="M6 44 L58 30 L62 68 L22 70 L34 56 Z" fill="var(--ribbon-fold)"/>
      <path d="M278 44 L226 30 L222 68 L266 82 L250 58 Z" fill="var(--ribbon-fold)"/>
      <path d="M46 22 Q142 -2 238 22 L236 60 Q142 38 48 60 Z" fill="var(--ribbon)"/>
    </svg>
    <span class="ribbon__label">Mirvana’s Treats</span>
  </div>
  <div class="flourish flourish--name" role="img" aria-label="Small scroll ornament"></div>

  <section class="contact-panel">
    <ul class="contact-list">
      <li><span class="contact-list__dot"></span>friendspot.net/mirvana</li>
      <li><span class="contact-list__dot"></span>snapgrove.net/mirvanaliving</li>
      <li><span class="contact-list__dot"></span>mirvanaliving@orbelmail.com</li>
      <li><svg width="11" height="12" viewBox="0 0 24 24" aria-hidden="true"><path fill="#4f4640" d="M6.6 10.8a15 15 0 0 0 6.6 6.6l2.2-2.2c.3-.3.7-.4 1-.2 1.1.4 2.3.6 3.6.6.6 0 1 .4 1 1V20c0 .6-.4 1-1 1A17 17 0 0 1 3 4c0-.6.4-1 1-1h3.5c.6 0 1 .4 1 1 0 1.3.2 2.5.6 3.6.1.3 0 .7-.2 1z"/></svg>00971 552 47 31 69</li>
    </ul>
  </section>
  <figure class="photo photo--cake"><div class="photo__fill" role="img" aria-label="Photo of a chocolate cupcake"></div></figure>
</main>
</body>
</html>
```